Business Card for my New Brokerage

Looking to get a business card design for my new Real Estate Brokerage.
I want it with Picture, Phone Number, Email, Website, Office Address
Name and Designation. Please add logo too.

Target Market(s)

Real Estate Investors or Home Buyers

Industry/Entity Type

Real Estate

Contact Information for Business Card

Name, Email, Phone Number, website, email, office address

Colors
EB3D1F
EC4F4E
F09395
F8D3D4
FCEDEE

Requirements
Must have
• Minimalistic, Clean, Modern, Photo
Nice to have
• White and Red Colors

```html
<!DOCTYPE html>
<html lang="en">
<head>
<meta charset="utf-8">
<title>Ember Realty Inc – Business Card</title>
<link rel="stylesheet" href="https://fonts.googleapis.com/css2?family=Montserrat:wght@700&family=Open+Sans:wght@400;600;700&display=swap">
<style>
  :root {
    --bg: #e9e9eb;
    --card-white: #ffffff;
    --brand-red: #cc1b22;
    --gold: #d9b45a;
    --gold-dark: #a7802c;
    --gold-light: #f3dc93;
    --photo-cream: #efeadc;
    --photo-beige: #d9ccaa;
    --photo-green: #b8c27a;
    --shadow: rgba(0,0,0,0.18);
  }
  * { box-sizing: border-box; margin: 0; padding: 0; }
  html, body { width: 1200px; height: 900px; overflow: hidden; }
  body {
    background: var(--bg);
    font-family: "Open Sans", sans-serif;
    display: flex;
    flex-direction: column;
    align-items: center;
    justify-content: center;
    gap: 44px;
  }
  .card {
    position: relative;
    width: 660px;
    height: 377px;
    overflow: hidden;
    background: var(--card-white);
    box-shadow: 0 10px 28px var(--shadow);
  }

  /* Front */
  .card-front__photo {
    position: absolute;
    inset: 0;
    background:
      radial-gradient(ellipse at 72% 38%, rgba(184,194,122,0.75) 0%, rgba(184,194,122,0) 45%),
      linear-gradient(120deg, var(--photo-cream) 0%, #f6f4ee 35%, var(--photo-beige) 70%, var(--photo-cream) 100%);
  }
  .brand-mark {
    position: absolute;
    display: flex;
    align-items: center;
    gap: 10px;
    font-family: "Montserrat", sans-serif;
    font-weight: 700;
    color: var(--brand-red);
    letter-spacing: 0.04em;
    text-transform: uppercase;
    white-space: nowrap;
  }
  .brand-mark__dot {
    width: 12px;
    height: 12px;
    background: var(--brand-red);
  }
  .card-front .brand-mark { right: 40px; top: 178px; font-size: 34px; }
  .card-back .brand-mark { right: 40px; top: 58px; font-size: 34px; }

  /* Back */
  .card-back__panel { position: absolute; inset: 0; }
  .contact {
    position: absolute;
    left: 52px;
    color: var(--gold);
  }
  .contact__role { top: 168px; font-size: 15px; color: #fbe9c8; }
  .contact__name {
    top: 188px;
    font-size: 19px;
    font-weight: 700;
    letter-spacing: 0.03em;
    text-transform: uppercase;
  }
  .contact__list {
    list-style: none;
    top: 240px;
    font-size: 14.5px;
    line-height: 24px;
  }
  .contact__list li, .contact__address {
    display: flex;
    align-items: flex-start;
    gap: 10px;
  }
  .contact__list svg, .contact__address svg { flex: none; margin-top: 5px; }
  .contact__address {
    top: 322px;
    font-size: 14.5px;
    line-height: 20px;
  }
</style>
</head>
<body>

  <section class="card card-front" aria-label="Business card front">
    <div class="card-front__photo" role="img" aria-label="Photo of a model house with rolled blueprints on a bright desk"></div>
    <div class="brand-mark"><span class="brand-mark__dot"></span>Ember Realty Inc</div>
  </section>

  <section class="card card-back" aria-label="Business card back">
    <svg class="card-back__panel" viewBox="0 0 660 377" preserveAspectRatio="none" aria-hidden="true">
      <defs>
        <linearGradient id="goldEdge" x1="0" y1="0" x2="1" y2="1">
          <stop offset="0" stop-color="#f3dc93"/>
          <stop offset="0.5" stop-color="#c99c3f"/>
          <stop offset="1" stop-color="#f0d585"/>
        </linearGradient>
      </defs>
      <polygon points="0,136 340,136 414,377 0,377" fill="url(#goldEdge)"/>
      <polygon points="0,146 332,146 403,377 0,377" fill="#cc1b22"/>
    </svg>

    <div class="brand-mark"><span class="brand-mark__dot"></span>Ember Realty Inc</div>

    <p class="contact contact__role">Director</p>
    <p class="contact contact__name">Daniel Hart</p>

    <ul class="contact contact__list">
      <li>
        <svg width="14" height="14" viewBox="0 0 24 24" fill="#d9b45a" aria-hidden="true"><path d="M6.6 10.8a15.1 15.1 0 0 0 6.6 6.6l2.2-2.2a1 1 0 0 1 1-.25 11.4 11.4 0 0 0 3.6.57 1 1 0 0 1 1 1V20a1 1 0 0 1-1 1A17 17 0 0 1 3 4a1 1 0 0 1 1-1h3.5a1 1 0 0 1 1 1c0 1.25.2 2.45.57 3.57a1 1 0 0 1-.25 1z"/></svg>
        0123456789
      </li>
      <li>
        <svg width="14" height="14" viewBox="0 0 24 24" fill="#d9b45a" aria-hidden="true"><path d="M3 5h18a1 1 0 0 1 1 1v12a1 1 0 0 1-1 1H3a1 1 0 0 1-1-1V6a1 1 0 0 1 1-1zm9 7.5L4 7.3V8l8 5.2L20 8v-.7z"/></svg>
        info@emberrealtyinc.com
      </li>
      <li>
        <svg width="14" height="14" viewBox="0 0 24 24" fill="none" stroke="#d9b45a" stroke-width="2" aria-hidden="true"><circle cx="12" cy="12" r="9"/><path d="M3 12h18M12 3c3 3.5 3 14.5 0 18M12 3c-3 3.5-3 14.5 0 18"/></svg>
        www.emberrealtyinc.com
      </li>
    </ul>

    <div class="contact contact__address">
      <svg width="14" height="16" viewBox="0 0 24 28" fill="#d9b45a" aria-hidden="true"><path d="M12 0a9 9 0 0 0-9 9c0 7 9 17 9 17s9-10 9-17a9 9 0 0 0-9-9zm0 12.5A3.5 3.5 0 1 1 12 5.5a3.5 3.5 0 0 1 0 7z"/></svg>
      <p>11 dummy city, dummy place<br>P.O Box 0000 Dummy Land</p>
    </div>
  </section>

</body>
</html>
```